Harrowby Wine Label - Design a front and smaller back label for an exclusive red wine

Harrowby Wines produces a very high quality, high priced wine from an old and prestigous vineyard in one of Australia's oldest, but smallest wine growing regions. The grapevines are old (like old men with gnarled arms and trunks) and they produce fewer grapes than younger vines but the grape quality (and thus wine quality) is magnificent and highly sought after as it produces wine of exceptional quality.
The vineyard was purchased by the Harrowby family in February 2010 from a multinational wine company who made wonderful, trophy winning wines for 10 years before the vineyard went into a decline.
The challenge is to produce 2 labels - a simple main front label that focuses on the Harrowby brand and a smaller, information rich, back label that relates the history of the vineyard.
The labels should have a white or charcoal grey background and impart tradition, quality, exclusivity and a little self indulgence which is why we want the family crest incorporated - the choice of font will help.
It might also impart a sense of fun so that it appeals to the 25-35 year old age bracket.
The label should be kept clean and simple not loud and busy. Preferred colours are black, grey and white. Red is fine if used sparingly

Here are the details:_

Front Label (115 long x 65-90mm wide)

Harrowby
Lanternwatch Reserve
2011
Mudgee
Wine of Australia 750ml

Back Label (dimensions to suit text and front label design; font size small; text in black so that it is readable in less than optimal light (eg candlelight at a restaurant table).

Harrowby
Lanternwatch Reserve 2011

This is the first release of The Lanternwatch’s Reserve – just 100 dozen bottles were made. The wine was made from Shiraz and 10% Cabernet Sauvignon grapes sourced from an iconic Mudgee vineyard that was established 1966 by Peter Vallis. In 1994, the vineyard known as ”Silver Hollow”, became the source of a decade of formidable, trophy winning wines under Tindalberg’s and later Quellwood’s ownership. The 20ha vineyard was purchased by Corin & Margaret Harrowby in 2010. The Silver Hollow name was retained by Quellwoods; no wine has been released under this label since the 2006 vintage.

The shaky old Shiraz vines are slowly being restored to full health using careful cane pruning techniques that stimulates fresh, new tissue growth, more even bunch sizes and better grape quality and consistency. The Shiraz grapes used in this wine were hand-picked from two rows of the first crop from the 46 year old, cane pruned vines. The 2011 Reserve is the first step to re-establish the traditions of a famous vineyard and one of Australia’s most sought after export wines.

“Deep and intense purple hues with aromas of ripe blackberry fruits, spice and eucalypt with rich chocolate complemented by subtle oak overtones. A rich and full bodied wine exhibiting a soft yet generous palate with plum, forest fruits and mint chocolate notes. A fine grained tannin structure displaying integrated oak characters adds to the complexity of the wine. This wine was aged for 18 months in a blend of new French oak hogsheads and one year old American hogsheads, crafting a blend with great structure and length of flavour which will develop into a Mudgee classic” – Lewis Farrant, Winemaker

13.5% Alc/Vol.
Contains approx 8.0 std drinks
Preservative (220) added

Harrowby Wines
Tallowbend Rd, Mudgee 2850
www.harrowbywines.example.au

Reason: My apologies to the designers who have kindly submitted some wonderful designs. I am trying to achieve a conscentious between shareholders. This is difficult as they are in different parts of the world and I have learned through this experience that opinions on wine labels are quite diverse!!! The feedback I have received so far indicates the following (1) A light or white background is preferred (2) The crest should not be a dominant part of the label (3) The label needs to be clean, fresh and uncomplicated (4) If red is used it should be in minor detail only (5) "Harrowby" should be distinctive. The font is difficult for us! (6) We are considering "The Lanternwatch" RESERVE instead of "Lanternwatch's" RESERVE (7) The text on the back label is too long; I will edit and re-upload Many thanks for your help and patience Kind regards Corin

Good Morning All,
I have edited the back label text to reduce the size of the label. A Word file with the changes has just been uploaded.
Cheers
Corin

Dear Designers,
Thank you all so very much for the wonderful selection of designs you have submitted my family have all been overwhelmed by the quality and skill level exhibited and we all appreciate you your efforts
Kindest regards
Corin

Target Market(s)

25-35 year old men and women of Australia, China, US & UK

Industry/Entity Type

Restaurant

Requirements
Must have
• Crest
Should not have
• Animals on the label

```html
<!DOCTYPE html>
<html lang="en">
<head>
<meta charset="utf-8">
<title>Harrowby Lanternwatch's Reserve 2011 – Front Label</title>
<link rel="stylesheet" href="https://fonts.googleapis.com/css2?family=Kaushan+Script&family=Italianno&family=Courgette&display=swap">
<style>
  :root {
    --ink: #0b0b0b;
    --paper: #ffffff;
    --wine-red: #c8102e;
    --crest-light: #e9e9e9;
    --crest-mid: #9a9a9a;
  }
  * { box-sizing: border-box; margin: 0; padding: 0; }
  html, body {
    width: 939px;
    height: 1200px;
    overflow: hidden;
    background: var(--ink);
  }
  .label {
    position: relative;
    width: 939px;
    height: 1200px;
    background: var(--ink);
    overflow: hidden;
  }
  .label-frame {
    position: absolute;
    inset: 0;
    width: 939px;
    height: 1200px;
  }
  .label-frame .field { fill: var(--paper); }
  .label-frame .swoosh {
    fill: none;
    stroke: var(--wine-red);
    stroke-width: 3;
  }
  .label-text {
    position: absolute;
    left: 0;
    width: 100%;
    text-align: center;
    white-space: nowrap;
    line-height: 1;
  }
  .brand-name {
    top: 168px;
    font-family: "Kaushan Script", cursive;
    font-size: 150px;
    color: var(--ink);
    letter-spacing: -2px;
  }
  .wine-name {
    top: 420px;
    font-family: "Courgette", cursive;
    font-size: 62px;
    color: var(--wine-red);
  }
  .vintage {
    top: 540px;
    font-family: "Courgette", cursive;
    font-size: 56px;
    color: var(--wine-red);
  }
  .region {
    top: 632px;
    font-family: "Italianno", cursive;
    font-size: 48px;
    color: var(--ink);
  }
  .crest {
    position: absolute;
    left: 386px;
    top: 711px;
    width: 188px;
    height: 362px;
  }
  .footer-line {
    top: 1122px;
    font-family: "Italianno", cursive;
    font-size: 52px;
    color: var(--paper);
    word-spacing: 4px;
  }
</style>
</head>
<body>
  <main class="label">
    <svg class="label-frame" viewBox="0 0 939 1200" aria-hidden="true">
      <path class="field" d="M0,240 Q470,-60 939,220 L939,1000 Q470,1242 0,915 Z"/>
      <path class="swoosh" d="M0,132 Q470,-86 939,163"/>
      <path class="swoosh" d="M0,265 Q460,-42 939,130"/>
      <path class="swoosh" d="M0,936 Q470,1240 939,972"/>
      <path class="swoosh" d="M0,989 Q560,1220 939,963"/>
    </svg>

    <h1 class="label-text brand-name">Harrowby</h1>
    <p class="label-text wine-name">Lanternwatch's Reserve</p>
    <p class="label-text vintage">2011</p>
    <p class="label-text region">Mudgee</p>

    <svg class="crest" viewBox="0 0 188 362" role="img" aria-label="Family crest: motto scroll, crown and shield with gates and fish">
      <defs>
        <linearGradient id="crestTone" x1="0" y1="0" x2="0" y2="1">
          <stop offset="0" stop-color="var(--crest-light)"/>
          <stop offset="1" stop-color="var(--crest-mid)"/>
        </linearGradient>
      </defs>
      <path d="M0,116 L188,116 L188,280 Q188,330 94,362 Q0,330 0,280 Z" fill="url(#crestTone)"/>
      <rect x="20" y="0" width="148" height="110" rx="20" fill="var(--crest-light)"/>
    </svg>

    <p class="label-text footer-line">Wine of Australia&nbsp; 750ml</p>
  </main>
</body>
</html>
```